Easy Business Card / Presentation Cover Design Project

We are looking for a business card design, covers for powerpoint presentations for investors, and possibly simple stationary for a Chicago real estate development firm. Our new logo is attached below.

We rehab and provide newly constructed homes. We are not a real estate brokerage firm (i.e., agents such as Meridale 47) and only operate in the Chicago area.

In terms of design, sophisticated and high end that would appeal to investors (theme should resemble investment banks, hedge funds, private equity rather than tech startup).

Target Market(s)

Investors, banks, financing sources

Industry/Entity Type

Real Estate

Requirements
Must have
• Two deliverables here. 1) Business card 2) Covers for powerpoint presentation.

Must be able to look sophisticated and high end when printed. Please think through the type of printing that will be needed. Would prefer something that can be printed in raised ink but digital is ok as well.

Will be printed on heavy paper.

Business Card: Horizontal Layout, no black backgrounds,

For presentation front cover, should include logo only. For back cover, should include contact info. Horizontal and should not contain any information that will need to be changed (i.e. date or client name)
Nice to have
• Would like to have the edges colored but not required. Please show multiple designs
Should not have
• Should not have any die cut or embossed type of designs. Shape should be standard size.

We are not a design firm, a retail firm, or a consumer product firm.

Please do not incorporate a house, buildings, etc. This must be very professional looking.

```html
<!DOCTYPE html>
<html lang="en">
<head>
<meta charset="utf-8">
<title>Halvern Realty – Business Cards</title>
<link rel="stylesheet" href="https://fonts.googleapis.com/css2?family=Questrial&family=Open+Sans:wght@700&display=swap">
<style>
  :root {
    --backdrop: #dcdad8;
    --card: #f7f7f6;
    --edge-blue: #2f6fd6;
    --brand-blue: #2b8fe6;
    --ink: #5a5a5a;
    --ink-strong: #4a4a4a;
    --rule: #9a9a9a;
  }
  * { margin: 0; padding: 0; box-sizing: border-box; }
  html, body { width: 1200px; height: 858px; overflow: hidden; }
  body {
    background: var(--backdrop);
    font-family: "Questrial", sans-serif;
    color: var(--ink);
    position: relative;
  }
  .card {
    position: absolute;
    width: 620px;
    height: 330px;
    background: var(--card);
    box-shadow:
      0 3px 0 #ffffff,
      0 5px 0 var(--edge-blue),
      0 7px 0 #ffffff,
      0 9px 0 var(--edge-blue),
      0 16px 24px rgba(0,0,0,0.18);
  }
  .card--front { left: 210px; top: 60px; }
  .card--back { left: 370px; top: 460px; }

  .brand {
    display: flex;
    align-items: center;
    gap: 14px;
    position: absolute;
  }
  .brand__dot {
    border-radius: 50%;
    background: var(--brand-blue);
    flex: none;
  }
  .brand__name {
    font-family: "Questrial", sans-serif;
    color: var(--ink-strong);
    line-height: 1;
    letter-spacing: 1px;
    white-space: nowrap;
  }
  .card--front .brand { left: 60px; top: 70px; }
  .card--front .brand__dot { width: 72px; height: 72px; }
  .card--front .brand__name { font-size: 34px; }

  .holder { position: absolute; text-align: right; white-space: nowrap; }
  .holder__name {
    font-family: "Open Sans", sans-serif;
    font-weight: 700;
    font-size: 17px;
    color: var(--ink-strong);
    letter-spacing: 0.5px;
  }
  .holder__title { font-size: 13px; }
  .card--front .holder { right: 60px; top: 146px; }

  .contact-row {
    position: absolute;
    left: 96px; right: 56px; bottom: 50px;
    display: flex;
    align-items: center;
    justify-content: space-between;
    font-size: 13px;
    line-height: 1.3;
    white-space: nowrap;
  }
  .contact-row__cell { flex: none; }
  .contact-row__divider { width: 1px; height: 32px; background: var(--rule); flex: none; }
  .contact-row__cell--phones { text-align: right; }
  .contact-row strong { font-family: "Open Sans", sans-serif; font-weight: 700; color: var(--ink-strong); }

  .card--back .brand { left: 70px; top: 128px; }
  .card--back .brand__dot { width: 80px; height: 80px; }
  .card--back .brand__name { font-size: 32px; }
  .card--back .divider-vertical {
    position: absolute; left: 345px; top: 66px; width: 1px; height: 196px; background: #cfcfcf;
  }
  .card--back .holder { left: 385px; top: 56px; text-align: left; }
  .details { position: absolute; left: 400px; top: 112px; list-style: none; font-size: 13px; white-space: nowrap; }
  .details li { display: flex; align-items: center; gap: 10px; height: 18px; }
  .details svg { width: 13px; height: 13px; flex: none; }
  .address { position: absolute; left: 425px; top: 214px; font-size: 13px; line-height: 1.3; white-space: nowrap; }
</style>
</head>
<body>
  <section class="card card--front">
    <div class="brand">
      <span class="brand__dot"></span>
      <span class="brand__name">HALVERN<br>REALTY</span>
    </div>
    <div class="holder">
      <div class="holder__name">MARTIN CRANE</div>
      <div class="holder__title">President</div>
    </div>
    <div class="contact-row">
      <div class="contact-row__cell">www.halvernrealty.com<br>info@halvernrealty.com</div>
      <div class="contact-row__divider"></div>
      <div class="contact-row__cell">42 Wexford Lane<br>Harlow Qld 4010</div>
      <div class="contact-row__divider"></div>
      <div class="contact-row__cell contact-row__cell--phones"><strong>Phone:</strong> (07) 5550 1234<br><strong>Fax:</strong> (07) 5550 1235</div>
    </div>
  </section>

  <section class="card card--back">
    <div class="brand">
      <span class="brand__dot"></span>
      <span class="brand__name">HALVERN<br>REALTY</span>
    </div>
    <div class="divider-vertical"></div>
    <div class="holder">
      <div class="holder__name">MARTIN CRANE</div>
      <div class="holder__title">President</div>
    </div>
    <ul class="details">
      <li><svg viewBox="0 0 14 14" fill="none" stroke="#2f6fd6" stroke-width="1.2"><circle cx="7" cy="7" r="6.3"/><rect x="5" y="3.5" width="4" height="7" rx="0.7"/></svg>(07) 5550 1234</li>
      <li><svg viewBox="0 0 14 14" fill="none" stroke="#2f6fd6" stroke-width="1.2"><circle cx="7" cy="7" r="6.3"/><path d="M4.5 4 Q4 7 7 9.8 Q9 10.5 10 9.6 L8.8 8.4 L8 9 Q6 8 5.2 6 L5.8 5.2 Z"/></svg>(07) 5550 1235</li>
      <li><svg viewBox="0 0 14 14" fill="none" stroke="#2f6fd6" stroke-width="1.2"><circle cx="7" cy="7" r="6.3"/><rect x="3.8" y="4.8" width="6.4" height="4.4"/><path d="M3.8 4.8 L7 7.3 L10.2 4.8"/></svg>info@halvernrealty.com.au</li>
      <li><svg viewBox="0 0 14 14" fill="none" stroke="#2f6fd6" stroke-width="1.1"><circle cx="7" cy="7" r="6.3"/><ellipse cx="7" cy="7" rx="2.6" ry="6.3"/><path d="M0.7 7 H13.3 M1.8 4 H12.2 M1.8 10 H12.2"/></svg>www.halvernrealty.com.au</li>
    </ul>
    <div class="address">42 Wexford Lane<br>Harlow Qld 4010</div>
  </section>
</body>
</html>
```